New and upgraded www.varbelfunds.com content & design financial markets

We need an upgrade of our site. The current site is www.varbelfunds.com
Navigation with full site map i.e. the user can select any page from any menu item.

The “Insights” (Insikter) page will remain as is except new design AND with far more possibilities to add thumbnails, picts, videos etc. The user will have to logon to be able to read the full story.

The “Produkter & Tjänster” (“How to invest” in current web) will contain about the same info as the current “How to invest” pages.

Some pages will contain one or more videos and or speaker supported “live” graphics which we will supply. The media content shall be easy to change.

The site will have two languages from start, English and Swedish. There will be more languages added within 1 year or slightly more.

All texts will be provided by us.

I’m attaching a PDF with suggested content for some of the new pages. However this is just content and absolutely no design. We need new design for the total of the site as well as for the graphics.

Expectation info:
These sites (Both major players in our business) can be used as inspiration:
https://www.tormidgebank.com/eu/en/
https://www.pellhartgroup.com/index.html

Below some opt-OUT and opt-IN graphic rules in connection with the Web supporting our business acumen and brand:

Opt-OUT:
- images similar to educational comic books - it signals an authoritarian approach where the customer is small (insubstantial).
- images that signal trading, cyber, mystery and fast-paced business. We are extremely long-term and invest in real companies
- avoid images containing coins, calculators and banknotes. We're not a savings bank company. or payment service-branch
- avoid images of large data flows, because we should not make facts complex, but simple and comprehensible
- avoid sensing pictures of photo models. We are real people who stand for our efforts. We're not going to hide.
- avoid pictures of suits and tie. They signal rigid-banking. We're smart-investment, flexible, adaptable. Rather curl up your sleeves and show that we’re building something valuable.
- avoid pictures of skyscrapers and cool bank pictures - because they signal the more old valuations of big capital and giant banks - that we are not at all. I know we've had clean facades before. As long as we're not talking about bank skyscrapers, I'm in.

Opt-IN
- pictures of Henrik in moderate amount - he is our symbol person
- films with Henrik and explaining graphical films - explaining and clarifying
- images of pedagogy that give the customer a sense of overview and insights that we give to the customers in our service
- illustrations that explain and deepen our work
- pictures and bars that in 3d illustrate our consistent results and stable delivery
- images that signal that we have a full grasp of data, flows and analyses - without the image becoming a space adventure
- use the logo as a grid, shape and colour.
- no genre portraits, rather pictures of real customers - which gives a sense of why they are customers here
- images that support our core i.e. is science, innovation, unrestricted thinking (“out of the box” – (don’t like that sentence)), smart-solutions, data-driven, client-cantered, flexible and adaptable to client needs and expectation.
- Solid - to be trustworthy in any economic climate
- Long term - consistent work and choices. No trading. Numbers talk
- Data-driven - real tech - combining years of work in finance with straight on tech

Presenting on the webpage:
The story in text and illustration
Show the truth - we have a great history to show and give space
Only numbers and graphs that has a meaning - no artificial numbers etc.

Target Market(s)

Europe

Coding

Coded - Design and coding required

Number of Pages Required

5+ page

Colors

Designer to choose colors to be used in the design.

Requirements
Must have
• Colours in line with www.varbelfunds.com

```html
<!DOCTYPE html>
<html lang="en">
<head>
<meta charset="utf-8">
<title>Varbel Funds</title>
<link href="https://fonts.googleapis.com/css2?family=Jost:wght@300;400;500&family=Lato:wght@300;400;700&family=Tinos:wght@700&family=Playfair+Display:ital@1&display=swap" rel="stylesheet">
<style>
:root{
  --navy:#0d1f78;
  --band:#27497f;
  --blue:#1b4db3;
  --ink:#333;
  --muted:#666;
  --pale:#e8ebf0;
  --white:#fff;
}
*{box-sizing:border-box;margin:0;padding:0}
html,body{width:1200px;height:3502px;overflow:hidden}
body{position:relative;font-family:'Lato',sans-serif;color:var(--ink);background:var(--white)}
.abs{position:absolute}
a{color:var(--navy);text-decoration:underline}
.more{font-size:12px;color:var(--navy)}
.more::after{content:"";display:inline-block;margin-left:7px;border-left:5px solid var(--navy);border-top:4px solid transparent;border-bottom:4px solid transparent}
.photo{position:absolute}

/* hero */
.hero{left:0;top:0;width:1200px;height:600px;background:linear-gradient(160deg,#8a8f93 0%,#4e5559 45%,#2c3235 100%)}
.nav{left:161px;top:37px;width:878px;height:60px;background:var(--white);display:flex;align-items:center;padding:0 14px}
.brand{display:flex;align-items:center;gap:8px;font-family:'Jost',sans-serif;font-size:26px;color:var(--navy);font-weight:400}
.brand .mark{width:20px;height:20px;background:var(--navy)}
.menu{margin-left:auto;display:flex;list-style:none;font-size:12px;color:#555;height:60px;align-items:center}
.menu li{padding:0 15px;border-left:1px solid #ccc;line-height:12px;position:relative}
.menu li:first-child{border-left:none}
.menu li.active::after{content:"";position:absolute;left:12px;right:12px;top:36px;height:3px;background:var(--navy)}
.search{width:12px;height:12px;margin-left:2px}
.hero-title{left:162px;top:260px;font-family:'Tinos',serif;font-size:42px;line-height:45px;color:var(--white);letter-spacing:.5px}
.hero-sub{left:162px;top:362px;font-size:13px;color:var(--white)}
.btn-line{display:inline-block;border:1px solid var(--white);color:var(--white);font-size:12px;padding:9px 16px}
.hero-btn{left:162px;top:401px;background:var(--blue)}
.form{left:776px;top:186px;width:263px;height:336px;background:var(--white);border-radius:10px;padding:20px 38px}
.form h3{font-family:'Playfair Display',serif;font-style:italic;font-weight:400;font-size:27px;color:var(--navy);text-align:center;margin-bottom:14px}
.field{font-size:10px;color:#888;border-bottom:1px solid #ccc;padding:10px 0 8px;margin-bottom:9px}
.send{margin-top:22px;width:112px;height:37px;background:var(--blue);color:var(--white);border-radius:4px 12px 4px 4px;font-size:12px;font-weight:700;letter-spacing:1px;display:flex;align-items:center;justify-content:center}

/* about */
.dots{left:532px;top:650px;width:156px;height:130px;background:#eef0f4}
.about-photo{left:160px;top:675px;width:412px;height:299px;background:linear-gradient(135deg,#c9a27a,#8d7a66 50%,#d8d2c8)}
.section-title{font-family:'Jost',sans-serif;font-weight:400;color:var(--navy);font-size:40px}
.about-text{left:770px;top:720px;width:270px}
.about-text p,.tb-text p{font-size:12px;line-height:22.5px;color:var(--muted);margin:12px 0 14px}
.feature{top:1050px;width:220px;text-align:center}
.feature .num{width:82px;height:82px;margin:0 auto;border-radius:50%;background:var(--pale);font-family:'Jost',sans-serif;font-size:32px;color:var(--navy);display:flex;align-items:center;justify-content:center;font-weight:500}
.feature h4{font-weight:400;font-size:15px;margin:15px 0 12px;color:#222}
.feature p{font-size:12px;line-height:19px;color:var(--muted);margin-bottom:14px}

/* approach */
.approach-title{left:162px;top:1425px;color:var(--white);font-size:40px}
.approach-text{left:162px;top:1489px;width:400px;font-size:12px;line-height:23px;color:var(--white)}
.approach-btn{left:162px;top:1553px}

/* cards */
.card{top:1752px;width:278px;height:150px;border:1px solid var(--band);background:var(--white);overflow:hidden}
.card svg.tri{position:absolute;left:0;top:0}
.card .ico{position:absolute;left:10px;top:58px;width:34px;height:34px}
.card h5{position:absolute;left:83px;top:16px;width:190px;font-weight:400;font-size:13.5px;line-height:22px;color:var(--navy)}
.card hr{position:absolute;left:83px;right:20px;top:70px;border:none;border-top:1px solid #ddd}
.card p{position:absolute;left:83px;top:88px;width:190px;font-size:11px;line-height:18.5px;color:var(--muted)}
.card.dark{background:var(--band)}
.card.dark h5,.card.dark p{color:var(--white)}
.card.dark hr{border-color:#6f88b0}

/* thinking beyond */
.tb-photo{left:0;top:1978px;width:600px;height:375px;background:linear-gradient(120deg,#e9ecef,#a7aeb6 45%,#6d6a66 70%,#d9dde2)}
.tb-mark{left:548px;top:2108px;width:104px;height:140px;background:var(--navy)}
.tb-text{left:770px;top:2057px;width:275px}

/* philosophy */
.col{top:2428px;width:428px;height:337px;background:var(--pale)}
.col h3{height:52px;background:var(--band);color:var(--white);font-family:'Jost',sans-serif;font-weight:400;font-size:22px;display:flex;align-items:center;justify-content:center}
.col ul{list-style:none;padding:38px 20px 0 45px}
.col li{position:relative;font-size:12px;line-height:18px;color:#333;margin-bottom:10px}
.col li::before{content:"";position:absolute;left:-24px;top:6px;width:7px;height:7px;background:var(--navy)}
.col li.sub{margin-left:23px}
.col li.sub::before{border-radius:50%;width:5px;height:5px;left:-20px}

/* gallery */
.tile{top:2896px;width:270px;height:186px}
.tile span{position:absolute;left:16px;bottom:10px;color:var(--white);font-size:15px}

/* footer */
.foot-brand{left:162px;top:3213px}
.foot-about{left:162px;top:3255px;width:210px;font-size:11px;line-height:19px;color:var(--muted)}
.foot-col h6{font-family:'Jost',sans-serif;font-weight:400;font-size:15px;color:var(--navy);margin-bottom:18px}
.foot-col ul{list-style:none;font-size:11px;color:var(--muted)}
.foot-col li{margin-bottom:13.5px}
.contact li{display:flex;gap:10px;line-height:19px;margin-bottom:12px}
.contact svg{flex:none;margin-top:3px}
.socials{display:flex;gap:12px}
.socials span{width:37px;height:37px;border:1px solid #333;border-radius:50%}
.copy{left:0;top:3452px;width:1200px;height:50px;background:var(--band);color:var(--white);font-size:10px;text-align:center;padding-top:13px}
</style>
</head>
<body>

<section class="abs hero" role="img" aria-label="Business people meeting and shaking hands in a bright glass office lobby"></section>
<header class="abs nav">
  <div class="brand"><span class="mark"></span>Varbel Funds</div>
  <ul class="menu">
    <li class="active">Home</li><li>Philosophy</li><li>How to Invest</li><li>What we do</li><li>Insights</li><li>Login</li>
    <li><svg class="search" viewBox="0 0 12 12"><circle cx="5" cy="5" r="3.8" fill="none" stroke="#555" stroke-width="1.4"/><line x1="7.8" y1="7.8" x2="11" y2="11" stroke="#555" stroke-width="1.6"/></svg></li>
  </ul>
</header>
<h1 class="abs hero-title">OUR PERSONAL<br>INVESTMENT ADVISOR</h1>
<p class="abs hero-sub">Varbel Funds is Your Global Reference for Investment Advice</p>
<span class="abs btn-line hero-btn">LEARN MORE</span>
<form class="abs form">
  <h3>Getting Started</h3>
  <div class="field">Name*</div>
  <div class="field">Phone*</div>
  <div class="field">E-mail*</div>
  <div class="field">Message*</div>
  <div class="send">SEND</div>
</form>

<div class="abs dots" role="img" aria-label="Soft square grid backdrop"></div>
<div class="abs about-photo" role="img" aria-label="Advisors shaking hands across a meeting table with colleagues"></div>
<div class="abs about-text">
  <h2 class="section-title">ABOUT US</h2>
  <p>We are a privately held firm dedicated to clients who have entrusted us with their wealth. We act solely and transparently in the best interest of our clients. We pride ourselves on our discretion and confidentiality.</p>
  <a class="more">Learn More</a>
</div>

<div class="abs feature" style="left:200px"><div class="num">01</div><h4>Why Choose Us</h4><p>We secure your interests by<br>continuously keeping your<br>Investment optimal</p><a class="more">Learn More</a></div>
<div class="abs feature" style="left:508px"><div class="num">02</div><h4>Investment Intelligence</h4><p>Tailor-made Solutions to Preserve<br>and Grow Wealth in All Market<br>Conditions.</p><a class="more">Learn More</a></div>
<div class="abs feature" style="left:807px"><div class="num">03</div><h4>Client Focus</h4><p>We are dedicated to offer you<br>exceptional service and unbiased<br>financial advice.</p><a class="more">Learn More</a></div>

<svg class="abs" style="left:0;top:1330px" width="1200" height="380" viewBox="0 0 1200 380">
  <polygon points="0,80 160,32 1200,32 1200,292 1040,331 0,331" fill="var(--band)"/>
  <g fill="none" stroke="#4a6a9c" stroke-width="1.2">
    <rect x="236" y="52" width="20" height="20" transform="rotate(45 246 62)"/>
    <rect x="633" y="55" width="14" height="14" transform="rotate(45 640 62)"/>
    <rect x="66" y="167" width="14" height="14" transform="rotate(45 73 174)"/>
    <rect x="298" y="279" width="14" height="14" transform="rotate(45 305 286)"/>
    <rect x="573" y="283" width="14" height="14" transform="rotate(45 580 290)"/>
  </g>
  <circle cx="856" cy="179" r="182" fill="#e8edf4"/>
  <circle cx="856" cy="179" r="176" fill="#b9c8dc" role="img" aria-label="Advisor showing a tablet to a client"/>
</svg>
<h2 class="abs section-title approach-title">Our Approach</h2>
<p class="abs approach-text">Varbel Funds is truly different – We deliver Investment Services that sets us apart from our contemporaries</p>
<span class="abs btn-line approach-btn">LEARN MORE</span>

<div class="abs card" style="left:161px">
  <svg class="tri" width="60" height="150"><polygon points="0,0 60,75 0,150" fill="var(--band)"/></svg>
  <svg class="ico" viewBox="0 0 34 34" fill="none" stroke="#fff" stroke-width="1.3"><rect x="5" y="6" width="24" height="16" rx="2"/><circle cx="17" cy="14" r="4"/><line x1="10" y1="28" x2="24" y2="28"/></svg>
  <h5>Varbel Investment Management System VIMS®</h5><hr><p>Built on a combination of macroeconomic and fundamental analysis</p>
</div>
<div class="abs card dark" style="left:461px">
  <svg class="tri" width="60" height="150"><polygon points="0,0 60,75 0,150" fill="#fff"/></svg>
  <svg class="ico" viewBox="0 0 34 34" fill="none" stroke="var(--band)" stroke-width="1.3"><circle cx="17" cy="17" r="5"/><circle cx="17" cy="5" r="3"/><circle cx="17" cy="29" r="3"/><circle cx="5" cy="17" r="3"/><circle cx="29" cy="17" r="3"/></svg>
  <h5>VIQS ® Investment Generator</h5><hr><p>Varbel iQ Software VIQS® is designed analyse, forcast, generate and an infinite number of personalized.</p>
</div>
<div class="abs card" style="left:762px">
  <svg class="tri" width="60" height="150"><polygon points="0,0 60,75 0,150" fill="var(--band)"/></svg>
  <svg class="ico" viewBox="0 0 34 34" fill="none" stroke="#fff" stroke-width="1.3"><rect x="8" y="8" width="18" height="18" rx="2"/><line x1="13" y1="3" x2="13" y2="31"/><line x1="21" y1="3" x2="21" y2="31"/><line x1="3" y1="17" x2="31" y2="17"/></svg>
  <h5 style="top:30px">Services</h5><hr><p>VIMS® &amp; VIQS® enable Varbel Funds customized services &amp; solutions to low cost &amp; risks with predictable.</p>
</div>

<div class="abs tb-photo" role="img" aria-label="Smiling team of colleagues gathered together in an office"></div>
<div class="abs tb-mark"></div>
<div class="abs tb-text">
  <h2 class="section-title">Thinking Beyond</h2>
  <p>We asked ourselves – is this really how wealth management and investing should work? Is it really necessary to treat clients as just a number in a box? Is this how services should be delivered? How about flexibility?</p>
  <a class="more">Learn More</a>
</div>

<div class="abs col" style="left:161px">
  <h3>Varbel Investment Advisory Philosophy</h3>
  <ul>
    <li>Systematic Adaption to Market Climate</li>
    <li>Attractive Risk Returns with Low Portfolio Turnover</li>
    <li>Europe and U.S. Investment Area</li>
    <li>Built to Follow or Outperform the Market During Upturns and Avoid Large Declines During Long – Term Market Turndowns</li>
    <li>Long – Term Investment Strategy</li>
    <li>Continuously Monitoring, Identifying and Implementing to Maintain Optimal Portfolio</li>
  </ul>
</div>
<div class="abs col" style="left:611px">
  <h3>Varbel Funds Investment Strategy</h3>
  <ul>
    <li>Excellent Historic Performance</li>
    <li>Value Invest</li>
    <li class="sub">Macro</li>
    <li class="sub">Fundamental</li>
    <li>Active Management</li>
    <li>Risk Control</li>
    <li>Low Portfolio Turnover</li>
    <li>Portfolio Management on clients own account</li>
  </ul>
</div>

<svg class="abs" style="left:0;top:2837px" width="1200" height="303" viewBox="0 0 1200 303">
  <polygon points="0,0 1040,0 1200,30 1200,302 160,302 0,263" fill="var(--band)"/>
  <g fill="none" stroke="#4a6a9c" stroke-width="1.2">
    <rect x="408" y="20" width="20" height="20" transform="rotate(45 418 30)"/>
    <rect x="1001" y="23" width="14" height="14" transform="rotate(45 1008 30)"/>
    <rect x="54" y="84" width="14" height="14" transform="rotate(45 61 91)"/>
    <rect x="1142" y="140" width="14" height="14" transform="rotate(45 1149 147)"/>
    <rect x="724" y="260" width="14" height="14" transform="rotate(45 731 267)"/>
  </g>
</svg>
<div class="abs tile" style="left:161px;background:linear-gradient(135deg,#dfe5ec,#8aa6cf)" role="img" aria-label="Hand pointing at a chart on a tablet"><span>Make a Change!</span></div>
<div class="abs tile" style="left:465px;background:linear-gradient(135deg,#cfd3d6,#3b4552)" role="img" aria-label="Desk with monitors showing market charts"><span>Investment Intelligence</span></div>
<div class="abs tile" style="left:769px;background:linear-gradient(135deg,#6b86a8,#1f3554)" role="img" aria-label="Hand holding a magnifier over a network of client icons"><span>Client Focus</span></div>

<div class="abs brand foot-brand" style="font-size:28px"><span class="mark" style="width:22px;height:22px"></span>Varbel Funds</div>
<p class="abs foot-about">Lorem Ipsum is simply dummy text of the printing and typesetting industry Lorem Ipsum is simply dummy.</p>
<div class="abs foot-col" style="left:413px;top:3208px">
  <h6>Quick Links</h6>
  <ul><li>Home</li><li>Investment Intelligence</li><li>Thinking Beyond</li><li>What We Do</li><li>Login</li><li>Disclaimer</li><li>Contact Us</li></ul>
</div>
<div class="abs foot-col contact" style="left:613px;top:3208px;width:180px">
  <h6>Contact Us</h6>
  <ul>
    <li><svg width="10" height="13" viewBox="0 0 10 13"><path d="M5 0a5 5 0 0 1 5 5c0 3-5 8-5 8S0 8 0 5a5 5 0 0 1 5-5z" fill="var(--navy)"/><circle cx="5" cy="5" r="2" fill="#fff"/></svg>101 -Lorem Ipsum is simply dummy text of the printing</li>
    <li><svg width="11" height="11" viewBox="0 0 11 11"><path d="M2 0l2 2.5-1.2 1.5a7 7 0 0 0 4.2 4.2L8.5 7 11 9l-1.5 2C4.5 11 0 6.5 0 1.5z" fill="var(--navy)"/></svg>123 456 7890</li>
    <li><svg width="12" height="9" viewBox="0 0 12 9"><rect width="12" height="9" fill="var(--navy)"/><path d="M0 0l6 5 6-5" fill="none" stroke="#fff"/></svg>info@varbelfunds.com</li>
  </ul>
</div>
<div class="abs foot-col" style="left:838px;top:3208px">
  <h6>Follow Us</h6>
  <div class="socials"><span aria-label="Social profile 1"></span><span aria-label="Social profile 2"></span><span aria-label="Social profile 3"></span><span aria-label="Social profile 4"></span></div>
</div>
<div class="abs copy">© 2019 Varbel Funds | All rights Reserved</div>

</body>
</html>
```